Brava-Lux.ch is looking for business card letterhead and envelope C5 with WOW effect

We need a strong business card for our company Brava-Lux.ch, logo is available. You want a black or dark background on which the logo Stark r% 26 # 252; appears. Letterhead and envelope in C5 format should be in a similar design, but does not have to be We need a strong business card for our company Brava-Lux.ch, logo is available. A black or dark background is desired, on which the logo Stark comes across. The letterhead and the envelope in C5 format should have a similar design.

Target Market(s)

Private customers as well as entrepreneurs

Contact Information for Business Card

E-mail: info@brava-lux.ch
Web.www.Brava-Lux.ch
Tel: +41 ( 0 ) 79 384 6027
Adresse:
Kellerweg 14
9405 Ostheim

Hier kann man Icons verwenden für Email,Tel und Adressse

Font styles to use
Other font styles liked:
• Dubai,bold

Colors

Designer to choose colors to be used in the design.

Requirements
Must have
• WOW effect
Nice to have
• R% 26 # 252; back business card with our service listings. - VEHICLE LABELING - SHOP WINDOW LABELING - STICKERS AND MUCH MORE ... in red color

```html
<!DOCTYPE html>
<html lang="en">
<head>
<meta charset="utf-8">
<title>Brava-Lux.ch Business Card</title>
<link rel="stylesheet" href="https://fonts.googleapis.com/css2?family=Exo+2:wght@600&family=Montserrat:wght@400;500&display=swap">
<style>
  :root {
    --stage: #2a2a2b;
    --card: #1c1c1d;
    --card-edge: #161617;
    --accent: #f5c518;
    --text-light: #f1f1f1;
    --text-silver: #a9a9ab;
    --divider: #6a6a6a;
  }
  * { margin: 0; padding: 0; box-sizing: border-box; }
  html, body {
    width: 1200px; height: 874px; overflow: hidden;
    background: var(--stage);
  }
  .canvas {
    position: relative; width: 1200px; height: 874px;
    display: flex; flex-direction: column; align-items: center; justify-content: center;
    gap: 32px;
  }
  .card {
    position: relative; width: 620px; height: 354px;
    background: var(--card);
    box-shadow: 0 10px 30px rgba(0,0,0,.45);
    overflow: hidden;
  }
  /* Front */
  .card-front { display: flex; align-items: center; justify-content: center; gap: 18px; }
  .brand-dot {
    width: 26px; height: 26px; border-radius: 50%;
    background: var(--text-silver);
  }
  .brand-name {
    font-family: "Exo 2", sans-serif; font-weight: 600;
    font-size: 42px; letter-spacing: 1px; text-transform: uppercase;
    color: var(--text-silver);
  }
  /* Back */
  .network-field {
    position: absolute; inset: 0;
    background: radial-gradient(ellipse at 55% 60%, #262420 0%, var(--card) 70%);
  }
  .identity {
    position: absolute; right: 330px; top: 142px; text-align: right;
  }
  .person-name {
    font-family: "Exo 2", sans-serif; font-weight: 600;
    font-size: 25px; color: var(--accent); letter-spacing: .3px;
  }
  .person-role {
    font-family: "Montserrat", sans-serif; font-weight: 500;
    font-size: 17px; color: var(--text-light); margin-top: 2px;
  }
  .divider {
    position: absolute; left: 310px; top: 140px;
    width: 1px; height: 96px; background: var(--divider);
  }
  .contact-list {
    position: absolute; left: 328px; top: 158px; list-style: none;
  }
  .contact-list li, .address {
    display: flex; align-items: center; gap: 9px;
    font-family: "Montserrat", sans-serif; font-weight: 500;
    font-size: 14.5px; color: var(--text-light); line-height: 23px;
  }
  .icon { width: 12px; height: 12px; fill: var(--accent); flex: none; }
  .address { position: absolute; left: 150px; top: 276px; }
</style>
</head>
<body>
<main class="canvas">
  <section class="card card-front" aria-label="Business card front">
    <span class="brand-dot"></span>
    <span class="brand-name">Brava-Lux.ch</span>
  </section>

  <section class="card card-back" aria-label="Business card back">
    <div class="network-field" role="img" aria-label="Faint golden polygon network pattern across the card"></div>

    <div class="identity">
      <p class="person-name">Lukas Brunner</p>
      <p class="person-role">President</p>
    </div>

    <span class="divider"></span>

    <ul class="contact-list">
      <li>
        <svg class="icon" viewBox="0 0 24 24"><path d="M6.6 10.8a15 15 0 0 0 6.6 6.6l2.2-2.2c.3-.3.7-.4 1-.2 1.1.4 2.3.6 3.6.6.6 0 1 .4 1 1V20c0 .6-.4 1-1 1C10.6 21 3 13.4 3 4c0-.6.4-1 1-1h3.5c.6 0 1 .4 1 1 0 1.3.2 2.5.6 3.6.1.3 0 .7-.2 1z"/></svg>
        +41 ( 0 ) 79 384 6027
      </li>
      <li>
        <svg class="icon" viewBox="0 0 24 24"><path d="M2 5h20v14H2z M2 5l10 7 10-7" /><path d="M2 5l10 7 10-7v2l-10 7L2 7z" fill="#1c1c1d"/></svg>
        info@brava-lux.ch
      </li>
      <li>
        <svg class="icon" viewBox="0 0 24 24"><circle cx="12" cy="12" r="10"/><path d="M2 12h20M12 2c3 3 3 17 0 20M12 2c-3 3-3 17 0 20" stroke="#1c1c1d" stroke-width="1.6" fill="none"/></svg>
        www.Brava-Lux.ch
      </li>
    </ul>

    <p class="address">
      <svg class="icon" viewBox="0 0 24 24"><path d="M12 2a7 7 0 0 0-7 7c0 5 7 13 7 13s7-8 7-13a7 7 0 0 0-7-7zm0 9.5A2.5 2.5 0 1 1 12 6.5a2.5 2.5 0 0 1 0 5z"/></svg>
      Kellerweg 14 9405 Ostheim
    </p>
  </section>
</main>
</body>
</html>
```